WP website design (Brisden)

We need a wordpress design for an established auction and real estate company based in Kentucky. The winning design will incorporate a professional color scheme with company logo in a clean layout with specified widgets. The design needs to consider that this will be developed on a responsive theme. Color is #307d84, with gray/black or other as an accent/highlight color.

Industry/Entity Type

Real Estate

Requirements
Must have
• Elelments of design need to consider that this site is going to be developed on a responsive theme.

Navigation:
1) Home 2) Current Auctions 3) Past Auctions 4) Meet the Staff 5) For Sellers 6) For Buyers 7) Testimonials 8) Contact Us

Colors will be the blue of logo plus black/gray or other accent color.

Slideshow will be prominent, please use stock real estate photo for initial image. Will have following in either header or sidebar: testimonials, social icons (FB, linkedin Twitter, RSS), Featured Auctions widget, newsletter signup form.

Footer will have contact info (below) and attached affiliation logos.
Brisden Auctions, Inc.
48710 Pomeroy Rd., Louisville KY 40199
dan.office@brisdenbid.example
Phone: (502) 555 0172

```html
<!DOCTYPE html>
<html lang="en">
<head>
<meta charset="utf-8">
<title>Brisden Auctions, Inc.</title>
<link href="https://fonts.googleapis.com/css2?family=Arapey&family=Arimo:ital,wght@0,400;0,700;1,400;1,700&family=Raleway:wght@500;600&display=swap" rel="stylesheet">
<style>
:root{
  --teal:#307d84;
  --orange:#f0ae3a;
  --orange-dark:#d99a2a;
  --body:#333;
  --page:#e6e6e6;
  --card:#fff;
  --line:#d9d9d9;
  --footer:#3b3b3b;
}
*{box-sizing:border-box;margin:0;padding:0}
html,body{width:924px;height:1200px;overflow:hidden}
body{position:relative;background:var(--page);font-family:"Arimo",Arial,sans-serif;color:var(--body)}
.abs{position:absolute}

/* header */
.site-header{left:0;top:0;width:924px;height:104px;background:linear-gradient(#f2f2f2,#fafafa)}
.brand{left:82px;top:34px;display:flex;align-items:center;gap:8px}
.brand-mark{width:22px;height:22px;background:var(--orange)}
.brand-name{font:700 25px/1 "Arimo",sans-serif;color:var(--teal)}
.social-label{left:498px;top:43px;font:26px/1 "Arapey",serif;color:#222;white-space:nowrap}
.social{top:36px;width:39px;height:39px;border-radius:50%}

/* nav */
.main-nav{left:0;top:104px;width:924px;height:38px;background:var(--teal);display:flex;justify-content:center}
.main-nav ul{display:flex;list-style:none;height:38px;margin-left:-2px}
.main-nav li{font:500 10.5px/38px "Raleway",sans-serif;color:#fff;padding:0 13px;border-left:1px solid rgba(255,255,255,.22)}
.main-nav li:first-child{border-left:0}
.main-nav li.active{color:var(--orange)}

/* hero */
.hero-band{left:0;top:142px;width:924px;height:339px;background:var(--orange)}
.slider{left:77px;top:161px;width:770px;height:296px;border:5px solid #8a5f1c;background:linear-gradient(#9bb4c8 0%,#d8d6c8 40%,#bfb79f 70%,#5e6a4a 85%,#8c8c8c 100%)}
.signup{left:104px;top:218px;width:244px;height:164px;background:rgba(20,20,20,.85);padding:14px 20px}
.signup h2{font:23px/1 "Arapey",serif;color:var(--orange);margin-bottom:6px}
.signup p{font:700 9.5px/1.35 "Arimo",sans-serif;color:#fff}
.signup .field{margin-top:12px;width:197px;height:21px;background:#fff;font:10px/21px "Arimo",sans-serif;color:#999;padding-left:6px}
.signup .btn{margin-top:18px;display:inline-block;padding:0 6px;height:25px;border:2px solid var(--teal);background:#fff;font:700 10px/21px "Arimo",sans-serif;color:#222}
.dropdown{left:421px;top:150px;width:159px;height:98px;background:rgba(240,225,200,.92);padding:16px 7px 0}
.dropdown div{height:23px;margin-bottom:6px;border-radius:3px;background:#3a3a3a;color:#fff;font:9.5px/23px "Arimo",sans-serif;padding-left:18px;position:relative}
.dropdown div::before{content:"";position:absolute;left:9px;top:8px;border:4px solid transparent;border-left:4px solid #fff;border-right:0}
.dropdown .on{background:var(--teal)}
.dropdown::before{content:"";position:absolute;left:73px;top:-7px;border:7px solid transparent;border-top:0;border-bottom-color:rgba(240,225,200,.92)}

/* cards */
.card{background:var(--card);border-radius:14px}
.intro{left:90px;top:517px;width:470px;font:10.5px/1.48 "Arimo",sans-serif;color:#444}
.intro strong{color:var(--teal)}
.cat-bar{left:84px;width:495px;height:24px;background:var(--teal);border-radius:4px;color:#fff;font:700 10.5px/24px "Arimo",sans-serif;padding-left:11px}
.lot{left:86px;width:491px;height:97px;border:1px solid var(--line);border-radius:4px}
.lot-photo{position:absolute;left:12px;top:8px;width:102px;height:79px;border:3px solid #fff;box-shadow:0 0 3px #999;background:linear-gradient(#4b5e3a,#7c8a6a 55%,#4f6b33)}
.lot h3{position:absolute;left:119px;top:14px;font:13.5px/1 "Arimo",sans-serif;color:var(--teal);letter-spacing:.2px}
.lot p{position:absolute;left:119px;top:34px;width:364px;font:9.2px/1.5 "Arimo",sans-serif;color:#222;text-align:justify}
.info{left:86px;width:491px;height:70px;border:1px solid var(--line);border-radius:4px}
.pill{position:absolute;left:17px;width:79px;height:22px;border-radius:4px;color:#fff;font:700 9.5px/22px "Arimo",sans-serif;padding-left:33px}
.pill svg{position:absolute;left:10px;top:6px}
.pill.details{top:8px;background:var(--orange)}
.pill.photos{top:37px;background:#333}
.info h4{position:absolute;left:118px;top:10px;font:11.5px/1 "Arimo",sans-serif;color:var(--teal)}
.info p{position:absolute;left:118px;top:32px;font:9.3px/1.5 "Arimo",sans-serif;color:#222}

/* sidebar */
.side-title{font:21px/1 "Arapey",serif;color:#222}
.news{left:624px;width:214px;height:62px;border-bottom:1px dotted #999}
.news .thumb{position:absolute;left:0;top:0;width:38px;height:38px;background:linear-gradient(#c9a98a,#7a5a40);border:1px solid #ddd}
.news p{position:absolute;left:43px;top:0;font:italic 8.8px/1.25 "Arimo",sans-serif;color:#333}
.news p b{font-style:normal;color:var(--teal)}
.news .date{position:absolute;right:2px;top:42px;font:italic 700 9.5px/1 "Arimo",sans-serif;color:var(--teal)}
.rule{height:1px;background:var(--line)}
.quote{left:628px;top:748px;width:192px;font:9.3px/1.42 "Arimo",sans-serif;color:#333}
.q{font:700 18px/1 "Arapey",serif;color:var(--teal);vertical-align:-4px}
.video{left:623px;top:885px;width:218px;height:157px;background:#111;padding:5px}
.video .frame{width:208px;height:136px;background:linear-gradient(#7e8fa3,#6f5a4a 50%,#3b3a40)}
.video .bar{margin-top:4px;height:5px;background:#444;border-radius:3px}

/* footer */
.site-footer{left:0;top:1095px;width:924px;height:80px;background:var(--footer)}
.contact{left:84px;top:1110px;font:10.5px/1.6 "Arimo",sans-serif;color:#fff;font-style:normal}
.badge{top:1108px;height:54px;background:#cfcfcf}
.copyright{left:0;top:1175px;width:924px;height:25px;background:var(--orange-dark);font:9.5px/25px "Arimo",sans-serif;color:#222;text-align:center}
</style>
</head>
<body>

<header class="site-header abs">
  <div class="brand abs"><span class="brand-mark"></span><span class="brand-name">Brisden Auctions inc.</span></div>
  <div class="social-label abs">Social Media:</div>
  <span class="social abs" style="left:658px;background:#1d4a75" aria-label="Social profile link"></span>
  <span class="social abs" style="left:707px;background:#1aa5e0" aria-label="Social profile link"></span>
  <span class="social abs" style="left:757px;background:#f29a13" aria-label="News feed link"></span>
  <svg class="social abs" style="left:805px" width="39" height="39" viewBox="0 0 39 39" aria-label="Email">
    <circle cx="19.5" cy="19.5" r="19.5" fill="#b5b5b5"/>
    <rect x="11" y="13" width="17" height="12" rx="1" fill="#fff"/>
    <path d="M11 14l8.5 6.5L28 14" fill="none" stroke="#b5b5b5" stroke-width="1.5"/>
  </svg>
</header>

<nav class="main-nav abs">
  <ul>
    <li>HOME</li><li>CURRENT AUCTIONS</li><li>PAST AUCTIONS</li><li>MEET THE STAFF</li>
    <li class="active">FOR SELLERS</li><li>FOR BUYERS</li><li>TESTIMONIALS</li><li>CONTACT US</li>
  </ul>
</nav>

<section class="hero-band abs"></section>
<div class="slider abs" role="img" aria-label="Stock photo of a two-storey residential building with lawn and parking lot"></div>

<form class="signup abs">
  <h2>Email Sign Up Form</h2>
  <p>Lorem ipsum dolor sit amet, consectetuer adipiscing elit. Nam</p>
  <div class="field">Email Address</div>
  <div class="btn">Subscribe Now</div>
</form>

<div class="dropdown abs">
  <div class="on">Lorem Ipsum is simply</div>
  <div>dummy text of the printing</div>
  <div>Typesetting industry.</div>
</div>

<main>
  <div class="card abs" style="left:77px;top:499px;width:509px;height:577px"></div>
  <p class="intro abs"><strong>simply dummy text of the printing and typesetting industry.</strong> Lorem Ipsum has been the industry's standard dummy text ever since the 1500s, when an unknown printer took a galley of type and scrambled it to make a type specimen book. It has survived not only five centuries, but also the leap into electronic typesetting, remaining essentially unchanged. It was popularised in the 1960s.</p>

  <div class="cat-bar abs" style="top:602px">VEHICLES * TRACTORS * FARM MACHINERY</div>
  <article class="lot abs" style="top:636px">
    <div class="lot-photo" role="img" aria-label="Photo of a white sedan parked on grass"></div>
    <h3>FURNITURE * ANTIQUES * COLLECTIBLES</h3>
    <p><b>HOUSE TRACT: 1 ½ Story frame home located on a 3.5 acre lot.</b> SMALL FARM TRACTS: Two tracts of 30.97 acres and 39.66 acres. BUILDING SITES: Two tracts of approximately five acres each with good frontage on Larkspur Road.</p>
  </article>
  <div class="info abs" style="top:741px">
    <span class="pill details"><svg width="17" height="10"><rect width="6" height="10" fill="#fff"/><rect x="8" y="1" width="9" height="2" fill="#fff"/><rect x="8" y="4" width="9" height="2" fill="#fff"/><rect x="8" y="7" width="9" height="2" fill="#fff"/></svg>Details</span>
    <span class="pill photos"><svg width="14" height="11"><rect x="0.5" y="0.5" width="13" height="10" fill="none" stroke="#fff"/><circle cx="7" cy="5.5" r="2.5" fill="#fff"/></svg>Photos</span>
    <h4>Live On-Site Auction</h4>
    <p>Begins:&nbsp; Saturday, June 08, 2013 at 10:00 AM EDT<br>Location: 8140 Larkspur Road&nbsp; Ashford, KY 40099</p>
  </div>

  <div class="cat-bar abs" style="top:845px">VEHICLES * TRACTORS * FARM MACHINERY</div>
  <article class="lot abs" style="top:879px">
    <div class="lot-photo" role="img" aria-label="Photo of a white sedan parked on grass"></div>
    <h3>FURNITURE * ANTIQUES * COLLECTIBLES</h3>
    <p><b>HOUSE TRACT: 1 ½ Story frame home located on a 3.5 acre lot.</b> SMALL FARM TRACTS: Two tracts of 30.97 acres and 39.66 acres. BUILDING SITES: Two tracts of approximately five acres each with good frontage on Larkspur Road.</p>
  </article>
  <div class="info abs" style="top:985px">
    <span class="pill details"><svg width="17" height="10"><rect width="6" height="10" fill="#fff"/><rect x="8" y="1" width="9" height="2" fill="#fff"/><rect x="8" y="4" width="9" height="2" fill="#fff"/><rect x="8" y="7" width="9" height="2" fill="#fff"/></svg>Details</span>
    <span class="pill photos"><svg width="14" height="11"><rect x="0.5" y="0.5" width="13" height="10" fill="none" stroke="#fff"/><circle cx="7" cy="5.5" r="2.5" fill="#fff"/></svg>Photos</span>
    <h4>Live On-Site Auction</h4>
    <p>Begins:&nbsp; Saturday, June 08, 2013 at 10:00 AM EDT<br>Location: 8140 Larkspur Road&nbsp; Ashford, KY 40099</p>
  </div>
</main>

<aside>
  <div class="card abs" style="left:612px;top:499px;width:235px;height:577px"></div>
  <h2 class="side-title abs" style="left:625px;top:513px">News &amp; Events</h2>
  <div class="news abs" style="top:546px">
    <div class="thumb" role="img" aria-label="Author thumbnail"></div>
    <p><b>simply dummy text of the</b><br>printing and typesetting industry. Lorem<br>Ipsum has been the industry's.</p>
    <span class="date">January 12, 2013</span>
  </div>
  <div class="news abs" style="top:621px;border-bottom:0">
    <div class="thumb" role="img" aria-label="Author thumbnail"></div>
    <p><b>simply dummy text of the</b><br>printing and typesetting industry. Lorem<br>Ipsum has been the industry's.</p>
    <span class="date">January 12, 2013</span>
  </div>
  <div class="rule abs" style="left:624px;top:691px;width:212px"></div>
  <h2 class="side-title abs" style="left:627px;top:708px">Testimonials</h2>
  <p class="quote abs"><span class="q">“</span> Ipsum has been the industry's standard dummy text ever since the 1500s, when an unknown printer took a galley of type and scrambled it to make a type specimen book. It has survived not only five centuries of type and scrambled it to make a type speci-men book. It has survived <span class="q">”</span></p>
  <div class="rule abs" style="left:624px;top:868px;width:212px"></div>
  <div class="video abs">
    <div class="frame" role="img" aria-label="Video still of an auctioneer speaking to a crowd"></div>
    <div class="bar"></div>
  </div>
  <svg class="abs" style="left:712px;top:930px" width="44" height="44" viewBox="0 0 44 44" aria-label="Play">
    <circle cx="22" cy="22" r="20" fill="rgba(0,0,0,.55)" stroke="#fff" stroke-width="3"/>
    <path d="M17 12l15 10-15 10z" fill="#fff"/>
  </svg>
</aside>

<footer>
  <div class="site-footer abs"></div>
  <address class="contact abs">Brisden Auctions, Inc.<br>48710 Pomeroy Rd., Louisville KY 40199<br>dan.office@brisdenbid.example&nbsp;&nbsp;&nbsp;Phone: (502) 555 0172</address>
  <span class="badge abs" style="left:514px;width:106px;border-radius:50%"></span>
  <span class="badge abs" style="left:630px;width:42px"></span>
  <span class="badge abs" style="left:688px;width:32px"></span>
  <span class="badge abs" style="left:736px;width:48px"></span>
  <span class="badge abs" style="left:797px;width:44px"></span>
  <div class="copyright abs">Copyright (c) Brisden Auctions, Inc. 2014. All Right Reserved</div>
</footer>

</body>
</html>
```